Business Card Re-Design...or logo does not look sharp

Hello

We are a start-up and just need someone to help us.

Our colors are: Marlowe Hush pink (yeah I know) and charcoal for the lettering.

I am attaching our logo which needs cleaning up.

We want the JUST the lady ironing on the table (pink) in front, and the background in charcoal. All the business info can be on the back.

Dims on card are 2 x 2''

Also, if you have better ideas....please let us know!

Thanks

Gregory

La Comadre Vapor
4827 Quellbrook Dr Suite B2
El Paso TX 79936
915-555-0148

```html
<!DOCTYPE html>
<html lang="en">
<head>
<meta charset="utf-8">
<title>La Comadre Vapor – Business Card</title>
<link rel="stylesheet" href="https://fonts.googleapis.com/css2?family=Dancing+Script:wght@400&display=swap">
<style>
  :root {
    --brand-pink: #ef3b6e;
    --charcoal: #4d4d4d;
    --lettering: #444444;
    --paper: #ffffff;
  }
  html, body {
    margin: 0;
    padding: 0;
    width: 1200px;
    height: 702px;
    overflow: hidden;
    background: var(--paper);
  }
  .business-card {
    position: relative;
    width: 1200px;
    height: 702px;
    overflow: hidden;
    background: var(--paper);
  }
  .card-artwork {
    position: absolute;
    inset: 0;
    width: 1200px;
    height: 702px;
    display: block;
  }
  .charcoal-field { fill: var(--charcoal); }
  .white-edge { fill: var(--paper); }
  .pink-wave { fill: var(--brand-pink); }
  .white-ground { fill: var(--paper); }
  .brand-square { fill: var(--brand-pink); }
  .brand-name {
    position: absolute;
    left: 536px;
    top: 540px;
    margin: 0;
    font-family: "Dancing Script", cursive;
    font-weight: 400;
    font-size: 68px;
    line-height: 1;
    color: var(--lettering);
    white-space: nowrap;
  }
</style>
</head>
<body>
  <main class="business-card">
    <svg class="card-artwork" viewBox="0 0 1085 630" preserveAspectRatio="none" xmlns="http://www.w3.org/2000/svg">
      <rect class="charcoal-field" x="0" y="0" width="1085" height="630" role="img" aria-label="Charcoal background with a white polka dot pattern"/>
      <path class="white-edge" d="M0,185 C60,120 160,90 270,92 C400,95 470,180 515,212 L590,215 C700,220 760,320 850,360 C950,395 1040,400 1085,405 L1085,630 L0,630 Z"/>
      <path class="pink-wave" d="M0,200 C60,135 160,105 270,107 C395,110 460,190 505,225 L590,228 C690,232 750,330 845,372 C945,408 1040,413 1085,418 L1085,630 L0,630 Z"/>
      <path class="white-ground" d="M0,300 C50,230 150,175 250,178 C360,182 440,250 500,285 C600,290 700,330 790,405 C870,440 1000,450 1085,458 L1085,630 L0,630 Z"/>
      <rect class="brand-square" x="150" y="258" width="285" height="285" role="img" aria-label="Pink silhouette of a girl ironing at a table"/>
    </svg>
    <h1 class="brand-name">La Comadre Vapor</h1>
  </main>
</body>
</html>
```